Flat Belly Design Graphics for Social

I want to create 9 social media graphics (new Instagram size 4:5 (1080 x 1350 pixels) focusing on our Flat Belly Graphics, using the pics attached. Use the attached pics, NO RANDOM STOCK PHOTOGRAPHY. For the color scheme of the graphics, the color palette is attached. YOU MUST POST ALL 9 GRAPHICS IN ONE ENTRY.
Using the 3 titles below, create one set of graphics. 1) with all text, then for the others, use the pictures as detailed below in IMPORTANT:
1. 21-Night Lean Middle Reboot Beyond 50
2. The 20-Second Trim-Core Menu Guide
3. Starlet Tricks to a Slender Midline Beyond 50 - Zero Scalpel Needed
IMPORTANT:
Only use RK Pic 1 and RK Pic 2 with the title, 21-Night Lean Middle Reboot Beyond 50
Only use meal plan1 and meal plan2 pics with the title, 20-Second Trim-Core Menu Guide
Only use starlet tricks 1 and starlet tricks 2 pics with the title, Starlet Tricks to a Slender Midline Beyond 50 - Zero Scalpel Needed
women over 40

```html
<!DOCTYPE html>
<html lang="en">
<head>
<meta charset="utf-8">
<title>Starlet Tricks to a Slender Midline Beyond 50</title>
<link rel="stylesheet" href="https://fonts.googleapis.com/css2?family=Montserrat:wght@800&family=Kaushan+Script&display=swap">
<style>
  :root {
    --bg-soft: #fbe9ef;
    --bg: #f8dde6;
    --ink-green: #2e4b48;
    --pink: #f27fae;
    --magenta: #c9508a;
    --skin-warm: #d9a78c;
    --denim: #5d86b3;
  }
  * { margin: 0; padding: 0; box-sizing: border-box; }
  html, body { width: 960px; height: 1200px; overflow: hidden; }
  body { background: var(--bg); }
  .poster {
    position: relative;
    width: 960px;
    height: 1200px;
    overflow: hidden;
    background: radial-gradient(ellipse 60% 50% at 50% 52%, var(--bg-soft) 0%, var(--bg) 100%);
  }
  .headline {
    position: absolute;
    left: 0; width: 100%;
    text-align: center;
    font-family: "Montserrat", sans-serif;
    font-weight: 800;
    color: var(--ink-green);
    font-size: 138px;
    line-height: 1;
    letter-spacing: -2px;
  }
  .headline--top { top: 62px; }
  .headline--bottom { top: 186px; }
  .script {
    position: absolute;
    left: 0; width: 100%;
    text-align: center;
    font-family: "Kaushan Script", cursive;
    color: var(--pink);
    line-height: 1;
  }
  .script--tagline { top: 292px; font-size: 86px; transform: rotate(-3deg); }
  .script--age { top: 405px; font-size: 80px; transform: rotate(-3deg); }
  .age-underline { position: absolute; left: 420px; top: 500px; }
  .subline {
    position: absolute;
    left: 0; width: 100%;
    top: 533px;
    text-align: center;
    font-family: "Montserrat", sans-serif;
    font-weight: 800;
    font-size: 40px;
    line-height: 1;
    color: var(--magenta);
  }
  .photo {
    position: absolute;
    left: 258px; top: 578px;
    width: 480px; height: 622px;
    border-radius: 200px 200px 0 0;
    background: linear-gradient(180deg, var(--skin-warm) 0%, #e2b8a6 55%, var(--denim) 100%);
    opacity: 0.85;
  }
</style>
</head>
<body>
  <main class="poster">
    <h1>
      <span class="headline headline--top">STARLET</span>
      <span class="headline headline--bottom">TRICKS</span>
    </h1>
    <p class="script script--tagline">to a Slender Midline</p>
    <p class="script script--age">Beyond 50</p>
    <svg class="age-underline" width="140" height="16" viewBox="0 0 140 16" aria-hidden="true">
      <path d="M4 12 Q70 -2 136 8" fill="none" stroke="#f27fae" stroke-width="4" stroke-linecap="round"/>
    </svg>
    <p class="subline">ZERO SCALPEL NEEDED</p>
    <div class="photo" role="img" aria-label="Photo of two smiling women in casual tops and jeans, one whispering a secret to the other"></div>
  </main>
</body>
</html>
```